Mr Pellowes Yard Works flyer for newsletter

I need a professional looking flyer design for my company Mr Pellowes Yard Works based in New Braunfels, TX to boost sales. Must include the following: Lawn service starting at $40 (mowing, edging, leaf blowing) Tree trimming starting at $125. Other services-mulching, shrub trimming, aeration, flower bed maintenance, Fall/spring clean up. Serving New Braunfels and surrounding areas. To set up and estimate please call 512 555 0143 or email mrpellowesyard@example-mail.net

Industry/Entity Type

Landscaping

Font styles to use
Serif

Colors

Designer to choose colors to be used in the design.

Requirements
Must have
• Phone number 512 555 0143
• Email mrpellowesyard@example-mail.net

```html
<!DOCTYPE html>
<html lang="en">
<head>
<meta charset="utf-8">
<title>Mr Pellowes Yard Works – Flyer</title>
<link rel="stylesheet" href="https://fonts.googleapis.com/css2?family=Open+Sans:ital,wght@0,400;0,600;0,700;0,800;1,400&display=swap">
<style>
  :root {
    --green: #4f8a1e;
    --green-dark: #3d6f15;
    --ink: #1f1f1f;
    --red: #e3202a;
    --paper: #ffffff;
  }
  * { margin: 0; padding: 0; box-sizing: border-box; }
  html, body { width: 927px; height: 1200px; overflow: hidden; background: var(--paper); }
  body { font-family: "Open Sans", Arial, sans-serif; color: var(--ink); }
  .flyer { position: relative; width: 927px; height: 1200px; background: var(--paper); }

  .brand { position: absolute; left: 70px; top: 62px; width: 270px; text-align: center;
           color: var(--green); font-weight: 800; line-height: 1; }
  .brand-small { display: block; font-size: 24px; margin-bottom: 6px; }
  .brand-large { display: block; font-size: 66px; letter-spacing: -1px; line-height: 0.98; }

  .offers { position: absolute; left: 480px; top: 58px; width: 410px; text-align: center; }
  .offer-title { color: var(--green); font-weight: 800; font-size: 40px; line-height: 1.1; }
  .offer-price { font-size: 35px; font-weight: 400; line-height: 1.15; letter-spacing: 0.5px; }
  .offer-price strong { color: var(--green); font-weight: 800; }
  .offer-tags { display: inline-block; margin-top: 6px; background: var(--green); color: #fff;
                font-weight: 600; font-size: 17.5px; padding: 3px 18px; width: 312px; }
  .offer-tree { margin-top: 36px; }

  .collage { position: absolute; left: 0; top: 300px; width: 927px; height: 485px; }

  .services { position: absolute; left: 44px; top: 800px; }
  .services h2 { font-size: 45px; font-weight: 600; margin-bottom: 8px; letter-spacing: -0.5px; }
  .service-list { list-style: none; }
  .service-list li { display: flex; align-items: center; gap: 14px; font-size: 29px; font-weight: 600;
                     height: 43px; }
  .tick { width: 34px; height: 34px; flex: none; }

  .contact { position: absolute; left: 508px; top: 866px; width: 356px; text-align: center; }
  .contact-lead { font-size: 19px; font-weight: 700; }
  .call-box { position: relative; margin: 34px auto 0; width: 322px; height: 72px;
              border: 2px solid var(--ink); }
  .call-label { position: absolute; top: -21px; left: 50%; transform: translateX(-50%);
                background: var(--paper); padding: 0 12px; font-size: 27px; font-weight: 600; white-space: nowrap; }
  .call-number { display: block; margin-top: 18px; color: var(--red); font-size: 38px; font-weight: 700; line-height: 1; letter-spacing: 0.5px; }
  .contact-email { margin-top: 12px; font-size: 19px; font-weight: 600; white-space: nowrap; }
  .contact-email em { font-weight: 400; }

  .footer-band { position: absolute; left: 0; top: 1111px; width: 927px; height: 49px;
                 background: var(--green); color: #fff; font-size: 18px; font-weight: 600;
                 display: flex; align-items: center; justify-content: center; }
</style>
</head>
<body>
<div class="flyer">

  <div class="brand">
    <span class="brand-small">Mr Pellowes</span>
    <span class="brand-large">Yard<br>Works</span>
  </div>

  <div class="offers">
    <div class="offer-title">LAWN SERVICE</div>
    <div class="offer-price">STARTING AT <strong>$40</strong></div>
    <div class="offer-tags">Mowing | Edging | Leaf blowing</div>
    <div class="offer-title offer-tree">TREE TRIMMING</div>
    <div class="offer-price">STARTING AT <strong>$125</strong></div>
  </div>

  <svg class="collage" viewBox="0 300 927 485" xmlns="http://www.w3.org/2000/svg">
    <defs>
      <linearGradient id="house" x1="0" y1="0" x2="0" y2="1">
        <stop offset="0" stop-color="#dfe6e3"/><stop offset="0.55" stop-color="#b9c7a8"/><stop offset="1" stop-color="#6fae2e"/>
      </linearGradient>
      <linearGradient id="hand" x1="0" y1="0" x2="0" y2="1">
        <stop offset="0" stop-color="#6b7a3a"/><stop offset="1" stop-color="#4d9a1d"/>
      </linearGradient>
      <linearGradient id="stripes" x1="0" y1="0" x2="0" y2="1">
        <stop offset="0" stop-color="#466b2a"/><stop offset="0.3" stop-color="#5f9a2a"/><stop offset="1" stop-color="#4f8f1c"/>
      </linearGradient>
      <linearGradient id="mower" x1="0" y1="0" x2="0" y2="1">
        <stop offset="0" stop-color="#a9c4cf"/><stop offset="0.45" stop-color="#4b5a4a"/><stop offset="1" stop-color="#74b03a"/>
      </linearGradient>
    </defs>
    <polygon points="0,303 416,300 348,592 0,592" fill="var(--green)"/>
    <polygon points="0,594 306,594 250,785 0,785" fill="var(--green)"/>
    <polygon points="386,358 927,358 927,785 240,785" fill="var(--green)"/>
    <polygon role="img" aria-label="Photo of a lawn specialist kneeling on a green lawn in front of a white house" points="0,307 410,305 343,589 0,589" fill="url(#house)"/>
    <polygon role="img" aria-label="Photo of a hand resting on freshly cut grass" points="0,597 302,597 247,780 0,780" fill="url(#hand)"/>
    <polygon role="img" aria-label="Photo of a striped mowed lawn with trees and fence" points="390,362 642,362 500,780 245,780" fill="url(#stripes)"/>
    <polygon role="img" aria-label="Close-up photo of a lawn mower wheel in tall grass" points="650,364 927,364 927,780 507,780" fill="url(#mower)"/>
  </svg>

  <section class="services">
    <h2>Other services</h2>
    <ul class="service-list">
      <li><svg class="tick" viewBox="0 0 34 34"><circle cx="16" cy="18" r="13" fill="none" stroke="#333" stroke-width="2.5"/><path d="M9 18 l6 6 L31 6" fill="none" stroke="#333" stroke-width="3" stroke-linecap="round" stroke-linejoin="round"/></svg>Mulching</li>
      <li><svg class="tick" viewBox="0 0 34 34"><circle cx="16" cy="18" r="13" fill="none" stroke="#333" stroke-width="2.5"/><path d="M9 18 l6 6 L31 6" fill="none" stroke="#333" stroke-width="3" stroke-linecap="round" stroke-linejoin="round"/></svg>Shrub trimming</li>
      <li><svg class="tick" viewBox="0 0 34 34"><circle cx="16" cy="18" r="13" fill="none" stroke="#333" stroke-width="2.5"/><path d="M9 18 l6 6 L31 6" fill="none" stroke="#333" stroke-width="3" stroke-linecap="round" stroke-linejoin="round"/></svg>Aeration</li>
      <li><svg class="tick" viewBox="0 0 34 34"><circle cx="16" cy="18" r="13" fill="none" stroke="#333" stroke-width="2.5"/><path d="M9 18 l6 6 L31 6" fill="none" stroke="#333" stroke-width="3" stroke-linecap="round" stroke-linejoin="round"/></svg>Flower bed maintenance</li>
      <li><svg class="tick" viewBox="0 0 34 34"><circle cx="16" cy="18" r="13" fill="none" stroke="#333" stroke-width="2.5"/><path d="M9 18 l6 6 L31 6" fill="none" stroke="#333" stroke-width="3" stroke-linecap="round" stroke-linejoin="round"/></svg>Fall/spring clean up</li>
    </ul>
  </section>

  <section class="contact">
    <p class="contact-lead">To Set up and Estimate</p>
    <div class="call-box">
      <span class="call-label">Please call</span>
      <span class="call-number">512 555 0143</span>
    </div>
    <p class="contact-email">or <em>email mrpellowesyard@example-mail.net</em></p>
  </section>

  <div class="footer-band">Serving New Braunfels and surrounding areas.</div>
</div>
</body>
</html>
```